Rental brochure for The Tallowcrest Vineyard

We need an A5 4 page brochure (A4 single fold) for a new real estate development in Sydney Australia called The Tallowcrest Vineyard. It is a residential development with cafe/restaurant, indoor swimming pool, gym and a heritage museum displaying machinery and artefacts from the property's former use as a winery producing champagne. The brochure is to be used in promoting rental of the individual dwellings which are 2 bedroom apartments and 3 bedroom town houses. Champagne, grape and similar motifs can be used but essentially it is about lifestyle. The property is positioned as middle market but is quite unique in its location presenting a level of luxury not available in that area. Concepts we feel good about include "champagne lifestyle" and "a new lease on life".
We will need a high res PDF of the finished product ready to upload to an online printer.
Our web site is: www.brenlofa.com.au
There is a short video on the project at: http://www.brenlofa.com.au/video4.htm
Updates
Project Deadline Extended
Reason: Copy now available.
Copy has now been uploaded and deadline extended. Thanks.
Target Market(s)
Young (mid thirties) semi-professional couples.
Industry/Entity Type
Real Estate
Look and feel

```html
<!DOCTYPE html>
<html lang="en">
<head>
<meta charset="utf-8">
<title>The Tallowcrest Vineyard – Brochure Back Cover</title>
<link rel="stylesheet" href="https://fonts.googleapis.com/css2?family=Montserrat:wght@300;400&display=swap">
<style>
  :root {
    --gold-light: #d4aa78;
    --gold-mid: #bf9868;
    --gold-edge: #a1855b;
    --card-highlight: #505052;
    --card-dark: #050505;
    --silver: #e4e4e6;
    --ornament: #9a9a9e;
    --contact-cream: #f5ebdc;
  }
  * { margin: 0; padding: 0; box-sizing: border-box; }
  html, body { width: 847px; height: 1200px; overflow: hidden; }
  body {
    font-family: "Montserrat", Arial, sans-serif;
  }
  .back-cover {
    position: relative;
    width: 847px;
    height: 1200px;
    background: radial-gradient(ellipse 70% 60% at 50% 42%, var(--gold-light) 0%, var(--gold-mid) 55%, var(--gold-edge) 100%);
    overflow: hidden;
  }
  .brand-card {
    position: absolute;
    left: 131px;
    top: 337px;
    width: 585px;
    height: 421px;
    background: radial-gradient(ellipse 90% 90% at 8% 5%, var(--card-highlight) 0%, #1c1c1d 45%, var(--card-dark) 100%);
    box-shadow: 0 10px 12px -4px rgba(40, 28, 10, 0.55);
  }
  .flourish {
    position: absolute;
    left: 116px;
    width: 353px;
    border-radius: 40px;
    background: var(--ornament);
    opacity: 0.3;
  }
  .flourish--top { top: 54px; height: 44px; }
  .flourish--bottom { top: 270px; height: 56px; }
  .brand-name {
    position: absolute;
    left: 0;
    right: 0;
    top: 118px;
    text-align: center;
    color: var(--silver);
    font-weight: 300;
    font-size: 52px;
    line-height: 45px;
    letter-spacing: 1px;
    text-transform: uppercase;
  }
  .contact {
    position: absolute;
    left: 0;
    right: 0;
    top: 893px;
    text-align: center;
    color: var(--contact-cream);
    font-weight: 300;
    font-size: 26px;
    line-height: 33.6px;
    font-style: normal;
    padding-left: 6px;
  }
</style>
</head>
<body>
  <main class="back-cover">
    <section class="brand-card">
      <div class="flourish flourish--top" role="img" aria-label="Silver ornamental scroll flourish above the name"></div>
      <h1 class="brand-name">The<br>Tallowcrest<br>Vineyard</h1>
      <div class="flourish flourish--bottom" role="img" aria-label="Silver ornamental scroll flourish below the name"></div>
    </section>
    <address class="contact">
      Brenlofa Property Network<br>
      Level 4, 316 Elmstone Road<br>
      Carrow&nbsp; NSW&nbsp; 2190<br>
      p: 02 5550 1840<br>
      f:&nbsp; 02 5550 1841<br>
      e: info@brenlofa.com.au
    </address>
  </main>
</body>
</html>
```